Introductory Flyer

We need a flyer to make businesses aware of our services. We do 3D Printing with a K540 Vantrix Printer(ie make solid prototypes from drawings.

We are a newish company looking to get new business. Photos and text can be taken from our website www.morlenfabworks.com.au and I have permision to use photos from www.vantrix.com if you need any extras. I could also write new text to suit your ideas.

3D Printing is a new technology.  People need to think "Hey! Look what this company can do for us."

Target Market(s)

Anyone designing or needing models of any solid object. Includes engineers, architects, councils, manufacturers. Need to send to businesses and get passed around rather than thrown out.

Industry/Entity Type

Manufacturing

Requirements
Must have
• Something quirky though not too expensive to print. Maybe folded popup card.

• Explain clearly what we actually do. ie 3D Printing and CAD Drawing.

• Not look out of accord with our website www.morlenfabworks.com.au

Nice to have
• Prefer smaller card to A4 sheet. Something to fit in DL envelope. Needs to convey quality and high tech side of our business.

```html
<!DOCTYPE html>
<html lang="en">
<head>
<meta charset="utf-8">
<title>Morlen Fabworks – 3D Printing Flyer</title>
<link rel="stylesheet" href="https://fonts.googleapis.com/css2?family=Open+Sans:wght@300;400;700&display=swap">
<style>
  :root {
    --orange: #e8601c;
    --orange-deep: #e2621e;
    --orange-pale: #fbe9dc;
    --paper: #ffffff;
    --ink: #2b2b2b;
    --ink-strong: #111111;
    --photo-light: #e9ebee;
    --photo-mid: #c9ccd0;
  }
  html, body {
    margin: 0;
    padding: 0;
    overflow: hidden;
    background: var(--paper);
  }
  .flyer {
    position: relative;
    width: 849px;
    height: 1200px;
    overflow: hidden;
    background: var(--paper);
    font-family: "Open Sans", sans-serif;
  }
  .photo {
    position: absolute;
    left: 0;
    width: 251px;
  }
  .photo--product {
    top: 0;
    height: 800px;
    background: linear-gradient(180deg, #f1f2f4 0%, var(--photo-light) 55%, var(--photo-mid) 100%);
  }
  .photo--heatmap {
    top: 800px;
    height: 223px;
    background: linear-gradient(135deg, #0f2a8a 0%, #1d5fd6 40%, #19b36b 62%, #e8451c 85%, #c8301a 100%);
  }
  .photo--wireframe {
    top: 1023px;
    height: 177px;
    background: linear-gradient(180deg, #f4f4f4 0%, #d8d8d8 100%);
  }
  .hero-panel {
    position: absolute;
    left: 251px;
    top: 0;
    width: 598px;
    height: 800px;
  }
  .headline {
    position: absolute;
    left: 284px;
    top: 136px;
    margin: 0;
    font-weight: 300;
    font-size: 45px;
    line-height: 42.5px;
    letter-spacing: -1.6px;
    color: var(--paper);
  }
  .headline .welcome { color: var(--orange); }
  .headline strong { font-weight: 700; letter-spacing: -1.4px; }
  .intro {
    position: absolute;
    left: 283px;
    top: 624px;
    width: 470px;
    margin: 0;
    font-weight: 300;
    font-size: 20px;
    line-height: 22.8px;
    letter-spacing: -0.8px;
    color: var(--paper);
  }
  .details {
    position: absolute;
    left: 283px;
    top: 818px;
    width: 540px;
    font-weight: 300;
    font-size: 19px;
    line-height: 22.8px;
    letter-spacing: -0.8px;
    color: var(--ink);
  }
  .details p { margin: 0 0 12px; }
  .cta {
    position: absolute;
    left: 283px;
    top: 1041px;
    width: 540px;
    margin: 0;
    font-weight: 700;
    font-size: 19.5px;
    line-height: 22.8px;
    letter-spacing: -0.7px;
    color: var(--ink-strong);
  }
</style>
</head>
<body>
<main class="flyer">
  <div class="photo photo--product" role="img" aria-label="Photo of a 3D printed garden sprinkler on a spike stand"></div>
  <div class="photo photo--heatmap" role="img" aria-label="Colour stress analysis render of a machined part"></div>
  <div class="photo photo--wireframe" role="img" aria-label="Black line wireframe CAD drawing of a vehicle"></div>

  <svg class="hero-panel" width="598" height="800" viewBox="0 0 598 800" aria-hidden="true">
    <defs>
      <linearGradient id="panelFade" x1="0" y1="0" x2="0" y2="1">
        <stop offset="0" stop-color="#ffffff"/>
        <stop offset="0.18" stop-color="#f9d9c3"/>
        <stop offset="0.6" stop-color="#ec9158"/>
        <stop offset="1" stop-color="#e2621e"/>
      </linearGradient>
    </defs>
    <polygon points="0,0 598,0 598,710 441,800 0,800" fill="url(#panelFade)"/>
  </svg>

  <h1 class="headline">
    <span class="welcome">Welcome to Morlen<br>Fabworks.</span><br>
    New <strong>3D Printing</strong><br>
    <strong>technology</strong> can jump<br>
    start your design<br>
    process by bringing<br>
    amazing <strong>high</strong><br>
    <strong>definition 3D models</strong><br>
    <strong>into your hands</strong> quickly<br>
    and affordably.
  </h1>

  <p class="intro">Using new 3D Printing technology we can jump start your design process by bringing amazing high definition 3D models into your hands quickly and affordably. These precision models are built up in very thin layers from computerised data such as a CAD drawing, an MRI scan or GIS data.</p>

  <section class="details">
    <p>3D parts created with this process are excellent for visual aids, prototypes, concept and evaluation models. No shape is too complex.</p>
    <p>You can evaluate your design in hours and check it for fit and feel, overcoming design errors without any expensive tooling costs.</p>
    <p>Get a head start in your design and sales process for that new product you’ve been thinking of. Morlen Fabworks offer a complete service including CAD drawing. You have the great idea. We’ll make it reality. Don’t just think it! Touch it! See it 3D!</p>
  </section>

  <p class="cta">Call 13 58 71 or email sales@morlenfabworks.com.au today and see how Morlen can move your vision into another dimension.</p>
</main>
</body>
</html>
```